New Business Card Design Project for Handyman Business

I would like to purchase a customized version of a design you have previously submitted - https://www.artvelloshowcase.com/design/58172046
I love this design!
I am hoping you can design something similar to this for our Handyman Business.
Attached is our logo and some graphics we have used.
Here is a link to the Google Doc with the content that needs to be included, https://files.quorvandel.net/document/d/e/4QZTR-8kPw2LmXn5Hb7rYcVt-qaaJsK3Df9TgNpU4WeR__LmcXaBvKpHsd2Qjn7wo4tzhgrVb41K85o3ttSTq/pub
Target Market(s)
Real Estate Agents, Home Owners and Property Managers
Industry/Entity Type
Construction/ Speciality Trade
Contact Information for Business Card
https://files.quorvandel.net/document/d/7QwRtYpL_zxkn4BvHnCdFs8TmKjWaEr2LUXPo6cxhg/edit?usp=sharing
Font styles to use
Other font styles liked:
- Ubuntu
Look and feel
Each slider illustrates characteristics of the customer's brand and the style your logo design should communicate.

```html
<!DOCTYPE html>
<html lang="en">
<head>
<meta charset="utf-8">
<title>Handcrest Business Card</title>
<link href="https://fonts.googleapis.com/css2?family=Ubuntu:wght@400;500;700&display=swap" rel="stylesheet">
<style>
  :root {
    --backdrop: #9a9a9a;
    --card-blue: #2378be;
    --card-blue-soft: #2a80c4;
    --brand-green: #4bb648;
    --accent-orange: #e8703a;
    --ink-light: #ffffff;
  }
  html, body {
    margin: 0;
    padding: 0;
    width: 1200px;
    height: 1000px;
    overflow: hidden;
    background: var(--backdrop);
    font-family: "Ubuntu", sans-serif;
  }
  .canvas { position: relative; width: 1200px; height: 1000px; }
  .card {
    position: absolute;
    top: 197px;
    width: 349px;
    height: 596px;
    border-radius: 18px;
    background: var(--card-blue);
    color: var(--ink-light);
    overflow: hidden;
    text-align: center;
  }
  .card--front { left: 180px; }
  .card--back { left: 624px; }
  .line { position: absolute; left: 0; right: 0; margin: 0; white-space: nowrap; }

  .brand-square {
    position: absolute; left: 50%; width: 40px; height: 40px;
    margin-left: -20px; background: var(--ink-light); border-radius: 3px;
  }
  .brand-name { font-weight: 500; font-size: 44px; line-height: 1; letter-spacing: 0.5px; }
  .brand-tagline {
    font-weight: 500; font-size: 13px; letter-spacing: 2.2px;
    color: var(--accent-orange);
  }
  .contact-name { font-weight: 700; font-size: 24px; }
  .contact-role { font-size: 17px; }
  .contact-detail { font-size: 19px; }
  .divider {
    position: absolute; left: 50%; width: 40px; height: 2px;
    margin-left: -20px; background: var(--ink-light);
  }
  .services { font-size: 15px; }
  .bullet {
    display: inline-block; width: 7px; height: 7px; margin: 0 4px 2px;
    background: var(--brand-green); transform: rotate(45deg);
    border: 1px solid var(--ink-light);
  }

  .pattern-field {
    position: absolute; inset: 0;
    background: linear-gradient(180deg, var(--card-blue-soft), var(--card-blue));
  }
  .social-row {
    position: absolute; top: 507px; left: 0; right: 0; height: 36px;
    display: flex; justify-content: center; align-items: center; gap: 6px;
  }
  .social-rule { width: 40px; height: 2px; background: var(--ink-light); margin: 0 5px; }
  .social-dot {
    width: 32px; height: 32px; border: 2px solid var(--ink-light); border-radius: 50%;
  }
  .hashtag { font-size: 18px; }
</style>
</head>
<body>
<div class="canvas">

  <section class="card card--front">
    <div class="brand-square" style="top:95px"></div>
    <p class="line brand-name" style="top:172px">handcrest</p>
    <p class="line brand-tagline" style="top:218px">HOME CARE SPECIALISTS</p>

    <p class="line contact-name" style="top:316px">MORGAN HALE</p>
    <p class="line contact-role" style="top:345px">Owner/ Handyman</p>
    <div class="divider" style="top:382px"></div>

    <p class="line contact-detail" style="top:408px">(555) 014-2738</p>
    <p class="line contact-detail" style="top:431px">morgan@handcrest-homes.com</p>
    <p class="line contact-detail" style="top:454px">Handcrest-homes.com</p>
    <div class="divider" style="top:496px"></div>

    <p class="line services" style="top:524px">Commercial and Resdiential Handyman</p>
    <p class="line services" style="top:546px">Improve<span class="bullet"></span>Repair<span class="bullet"></span>Remodel<span class="bullet"></span>Maintain</p>
  </section>

  <section class="card card--back">
    <div class="pattern-field" role="img" aria-label="Repeating faint brand pattern in soft blue tones"></div>
    <div class="brand-square" style="top:385px; width:32px; height:32px; margin-left:-16px"></div>
    <p class="line brand-name" style="top:437px">handcrest</p>
    <p class="line brand-tagline" style="top:482px">HOME CARE SPECIALISTS</p>
    <div class="social-row">
      <span class="social-rule"></span>
      <span class="social-dot"></span>
      <span class="social-dot"></span>
      <span class="social-dot"></span>
      <span class="social-dot"></span>
      <span class="social-rule"></span>
    </div>
    <p class="line hashtag" style="top:551px">#handcrestHandymanServices</p>
  </section>

</div>
</body>
</html>
```